Brisk Hive 360 Postcard Design, Double-Sided

Please read carefully and see attached. Designers that do not follow these instructions will not be selected. Limit ONE design submission per artist. The ONE design submission shall show both the front and the back designs. Designs must comply with the attached dismensions accounting for the bleed area to prevent designs from being cut off during printing. The attached business card and door tag designs have already been created, printed and are in use. The postcard shall be similar in design to the attached business card and door tag. All of the information that you need is attached. The overall size is 4.12" x 6.12" for the front. The back is different, see attached and scale to match template. I would like the Veteran Owned Business logo added as well. It would also be nice to see my photo incorporated somehow. I like the yellow on the door tag. It helps build contrast and pops out. Again, one design submission per designer that shows both the front and the back.

Target Market(s)

Please read all instructions and see attached.

Industry/Entity Type

Requirements
Must have
• Please read all instructions and see attached.
Nice to have
Should not have

```html
<!DOCTYPE html>
<html lang="en">
<head>
<meta charset="utf-8">
<title>Brisk Hive 360 Postcard</title>
<link rel="stylesheet" href="https://fonts.googleapis.com/css2?family=Lexend:wght@400;600&display=swap">
<style>
  :root {
    --red: #ec2227;
    --navy: #263271;
    --white: #ffffff;
    --ink: #1d1d22;
    --backdrop: #e4e5e8;
    --photo-light: #d9dadc;
    --photo-mid: #9ea3ad;
  }
  * { box-sizing: border-box; margin: 0; padding: 0; }
  html, body { width: 1200px; height: 1200px; overflow: hidden; background: var(--backdrop); }
  body { font-family: "Lexend", sans-serif; }
  .stage { position: absolute; left: 0; top: 0; width: 960px; height: 960px; transform: scale(1.25); transform-origin: 0 0; }
  .card { position: absolute; left: 166px; width: 627px; height: 422px; background: var(--white); overflow: hidden; box-shadow: 0 2px 8px rgba(0,0,0,.12); }
  .card--front { top: 44px; }
  .card--back { top: 494px; height: 421px; }
  .card-shapes { position: absolute; inset: 0; width: 100%; height: 100%; }
  .owner-photo { position: absolute; left: 38px; top: 36px; width: 110px; height: 128px; background: linear-gradient(180deg, var(--photo-light), var(--photo-mid)); }
  .highlights { position: absolute; left: 176px; top: 65px; list-style: none; color: var(--white); font-size: 13px; line-height: 17px; }
  .highlights li::before, .services-list li::before { content: "• "; }
  .owner-name { position: absolute; left: 38px; top: 196px; color: var(--white); font-weight: 600; font-size: 20px; }
  .owner-role { position: absolute; left: 38px; top: 222px; color: var(--white); font-size: 13px; }
  .partner-badge { position: absolute; left: 434px; top: 36px; width: 130px; height: 112px; }
  .services-title { position: absolute; left: 394px; top: 192px; color: var(--white); font-weight: 600; font-size: 22px; }
  .services-list { position: absolute; left: 394px; top: 238px; list-style: none; color: var(--white); font-size: 16px; line-height: 20.6px; }
  .contact { position: absolute; list-style: none; font-size: 14px; line-height: 21px; }
  .contact li { display: flex; align-items: center; gap: 11px; }
  .contact svg { width: 9px; height: 9px; flex: none; }
  .contact--front { left: 39px; top: 299px; color: var(--ink); }
  .contact--back { left: 52px; top: 293px; color: var(--white); }
  .brand { position: absolute; left: 51px; top: 40px; width: 119px; height: 119px; display: flex; flex-direction: column; align-items: center; justify-content: center; gap: 10px; }
  .brand-dot { width: 46px; height: 46px; border-radius: 50%; background: var(--ink); }
  .brand-name { font-weight: 600; font-size: 15px; color: var(--ink); }
  .stamp-box { position: absolute; left: 499px; top: 39px; width: 88px; height: 102px; border: 1.5px solid var(--ink); }
  .address-line { position: absolute; left: 374px; width: 213px; height: 1.5px; background: var(--ink); }
</style>
</head>
<body>
<div class="stage">
  <section class="card card--front">
    <svg class="card-shapes" viewBox="0 0 627 422" aria-hidden="true">
      <polygon fill="var(--red)" points="0,0 410,0 249,254 0,254"/>
      <polygon fill="var(--navy)" points="149,58 390,58 368,137 149,137"/>
      <polygon fill="var(--navy)" points="412,171 627,171 627,422 199,422"/>
    </svg>
    <div class="owner-photo" role="img" aria-label="Portrait photo of the owner"></div>
    <ul class="highlights">
      <li>Fast Response</li><li>High Quality</li><li>Fair Pricing</li><li>Veteran Owned</li>
    </ul>
    <h1 class="owner-name">Dalton R. Mereway</h1>
    <p class="owner-role">Owner &amp; Handyman</p>
    <svg class="partner-badge" viewBox="0 0 130 112" role="img" aria-label="Veteran owned business membership badge">
      <circle cx="65" cy="52" r="50" fill="var(--navy)"/>
      <circle cx="65" cy="52" r="41" fill="var(--white)"/>
      <rect x="4" y="64" width="122" height="18" fill="var(--red)"/>
    </svg>
    <h2 class="services-title">SERVICES:</h2>
    <ul class="services-list">
      <li>Assembly</li><li>Small Repairs</li><li>Wifi / Router Setup</li><li>Fabrication</li><li>Hanging Items</li><li>Wireless Device Setup</li><li>Odd Jobs</li>
    </ul>
    <ul class="contact contact--front">
      <li><svg viewBox="0 0 10 10"><circle cx="5" cy="3.5" r="2.5" fill="currentColor"/><path d="M1 10a4 4 0 0 1 8 0z" fill="currentColor"/></svg>Bayline, Florida</li>
      <li><svg viewBox="0 0 10 10"><rect x="0" y="2" width="10" height="7" fill="currentColor"/><path d="M0 2l5 4 5-4" stroke="var(--white)" fill="none"/></svg>service@briskhive360.com</li>
      <li><svg viewBox="0 0 10 10"><path d="M2 0l2 2-1 2a6 6 0 0 0 3 3l2-1 2 2-2 2C4 10 0 6 0 2z" fill="currentColor"/></svg>(555) 014-2290 Text</li>
      <li><svg viewBox="0 0 10 10"><circle cx="5" cy="5" r="4.3" fill="none" stroke="currentColor" stroke-width="1.2"/><path d="M0.7 5h8.6M5 0.7v8.6" stroke="currentColor"/></svg>briskhive360.com</li>
    </ul>
  </section>

  <section class="card card--back">
    <svg class="card-shapes" viewBox="0 0 627 421" aria-hidden="true">
      <polygon fill="var(--red)" points="0,173 290,266 290,280 0,186"/>
      <polygon fill="var(--navy)" points="0,186 290,280 290,421 0,421"/>
    </svg>
    <div class="brand">
      <span class="brand-dot"></span>
      <span class="brand-name">Brisk Hive 360</span>
    </div>
    <div class="stamp-box"></div>
    <div class="address-line" style="top:264px"></div>
    <div class="address-line" style="top:305px"></div>
    <div class="address-line" style="top:346px"></div>
    <ul class="contact contact--back">
      <li><svg viewBox="0 0 10 10"><circle cx="5" cy="3.5" r="2.5" fill="currentColor"/><path d="M1 10a4 4 0 0 1 8 0z" fill="currentColor"/></svg>Bayline, Florida</li>
      <li><svg viewBox="0 0 10 10"><rect x="0" y="2" width="10" height="7" fill="currentColor"/><path d="M0 2l5 4 5-4" stroke="var(--navy)" fill="none"/></svg>service@briskhive360.com</li>
      <li><svg viewBox="0 0 10 10"><path d="M2 0l2 2-1 2a6 6 0 0 0 3 3l2-1 2 2-2 2C4 10 0 6 0 2z" fill="currentColor"/></svg>(555) 014-2290 Text</li>
      <li><svg viewBox="0 0 10 10"><circle cx="5" cy="5" r="4.3" fill="none" stroke="currentColor" stroke-width="1.2"/><path d="M0.7 5h8.6M5 0.7v8.6" stroke="currentColor"/></svg>briskhive360.com</li>
    </ul>
  </section>
</div>
</body>
</html>
```